I need a Label design for my copper 71 kombucha brand that is launching soon

I want a label to go on my copper 71 kombucha bottle.
I have a logo image uploaded in the files but I am open to changes to this logo or even a completely New one if you think you can do better. This logo is based on the idea of an s-shaped naga. I particularly like the nagas from temples in luang prabang.
I also want to include the slogan - dare to be delicious.
The label should be some kind of oval at 80mm high by 70mm wide.
The label will go on a clear glass bottle. The kombucha will be visible and comes in different shades of red,yellow and purple.
The word kombucha should be clearly visible.
i want a very colorful, playful label. I'm very keen to see your ideas and I want something original.
Fermented foods and beverages

```html
<!DOCTYPE html>
<html lang="en">
<head>
<meta charset="utf-8">
<title>copper 71 — Kombucha Label</title>
<link rel="stylesheet" href="https://fonts.googleapis.com/css2?family=Questrial&family=Open+Sans:ital,wght@0,400;0,600;1,400&display=swap">
<style>
  :root {
    --backdrop-top: #c4c4c4;
    --backdrop-bottom: #ececec;
    --label-fill: #f2a233;
    --label-outline: #3b3f49;
    --info-band: #46494f;
    --brand-ink: #3b3f49;
    --brand-accent: #a3197a;
    --band-text: #f1f1f1;
  }
  html, body {
    margin: 0;
    padding: 0;
    width: 1200px;
    height: 1200px;
    overflow: hidden;
  }
  body {
    background: linear-gradient(to bottom, var(--backdrop-top), var(--backdrop-bottom));
  }
  .label {
    display: block;
    width: 1200px;
    height: 1200px;
  }
  .label__shape { fill: var(--label-fill); }
  .label__outline { fill: none; stroke: var(--label-outline); stroke-width: 5; }
  .label__band { fill: var(--info-band); }
  .brand__dot { fill: var(--brand-accent); }
  .brand__name {
    font-family: "Questrial", sans-serif;
    font-weight: 400;
    fill: var(--brand-ink);
  }
  .brand__rule { stroke: var(--brand-ink); stroke-width: 3; }
  .product__type {
    font-family: "Questrial", sans-serif;
    font-size: 38px;
    letter-spacing: 10px;
    fill: var(--brand-ink);
  }
  .product__slogan {
    font-family: "Open Sans", sans-serif;
    font-style: italic;
    font-size: 22px;
    fill: var(--brand-accent);
  }
  .band__copy {
    font-family: "Open Sans", sans-serif;
    font-size: 15.5px;
    fill: var(--band-text);
  }
  .band__volume {
    font-family: "Open Sans", sans-serif;
    font-weight: 600;
    font-size: 26px;
    fill: var(--band-text);
  }
</style>
</head>
<body>
<svg class="label" viewBox="0 0 1200 1200" xmlns="http://www.w3.org/2000/svg" aria-label="copper 71 kombucha label">
  <defs>
    <clipPath id="label-clip">
      <rect x="265" y="150" width="670" height="900" rx="320" ry="300"/>
    </clipPath>
  </defs>

  <rect class="label__shape" x="265" y="150" width="670" height="900" rx="320" ry="300"/>

  <g clip-path="url(#label-clip)">
    <rect class="label__band" x="250" y="810" width="700" height="260"/>
  </g>

  <rect class="label__outline" x="265" y="150" width="670" height="900" rx="320" ry="300"/>

  <g class="brand">
    <circle class="brand__dot" cx="600" cy="325" r="58"/>
    <text class="brand__name" x="600" y="530" font-size="128" text-anchor="middle">copper</text>
    <line class="brand__rule" x1="390" y1="618" x2="498" y2="618"/>
    <line class="brand__rule" x1="702" y1="618" x2="810" y2="618"/>
    <text class="brand__name" x="600" y="652" font-size="88" text-anchor="middle">71</text>
  </g>

  <g class="product">
    <text class="product__type" x="605" y="728" text-anchor="middle">KOMBUCHA</text>
    <text class="product__slogan" x="600" y="774" text-anchor="middle">dare to be delicious</text>
  </g>

  <g class="band">
    <text class="band__copy" text-anchor="middle">
      <tspan x="600" y="840">Lorem Ipsum is simply dummy text of the printing and typesetting</tspan>
      <tspan x="600" y="864">industry. Lorem Ipsum has been the industry's standard dummy text ever</tspan>
      <tspan x="600" y="888">since the 1500s, when an unknown printer took a galley of type and</tspan>
      <tspan x="600" y="912">scrambled it to make a type specimen book.</tspan>
    </text>
    <text class="band__volume" x="600" y="968" text-anchor="middle">100 ML</text>
  </g>
</svg>
</body>
</html>
```